DJ business brochure

I need a business brochure for my DJ business. Something that represents my business being owned and operated by first responders yet elegant enough to attract customers for weddings.

I do not have a preference on a type of brochure. Tri-fold or standard. The front page should have our logo and the name of our company. Under the name of our company it should say "Owned and operated by First Responders"

Bullet points for the brochure
LED up lighting.
Video projection
Dancing in the clouds
Top rated and experienced DJ's
Fun, crowd interactive DJ's
Text song request line.
Professional reception planning.

It should say somewhere on the brochure "When you choose Harbor 9 you become part of the first responder family."

Contact information Lou@harbor9dj.net Phone or text (507) 318-2674

Please use some fun pictures of weddings or people dancing. Does not specifically need to be from our sites.

Target Market(s)

Brides/Groom

Industry/Entity Type

Wedding/Party DJ

Requirements
Must have
• I want the wow factor. Something that when people look at the brochure they are drawn to read it. Email Lou@Harbor9DJ.net Phone (507) 318-2674
Nice to have
• Nice to have a flaming vinyl record or a flaming musical note somewhere in the brochure.

```html
<!DOCTYPE html>
<html lang="en">
<head>
<meta charset="utf-8">
<title>Harbor 9 – DJ Brochure</title>
<link href="https://fonts.googleapis.com/css2?family=Anton&family=Great+Vibes&family=Josefin+Sans:wght@400;600;700&display=swap" rel="stylesheet">
<style>
  :root{
    --bg:#e8e8e8;
    --paper:#f7f7f7;
    --night:#0b0a17;
    --navy:#1a1838;
    --violet:#3a3577;
    --red:#d01a1f;
    --deep-red:#8c0d12;
    --ink:#1c1c1c;
    --white:#ffffff;
  }
  *{box-sizing:border-box;margin:0;padding:0}
  html,body{width:1200px;height:1200px;overflow:hidden;background:var(--bg)}
  body{position:relative;font-family:"Josefin Sans",sans-serif;color:var(--ink)}
  .spread{position:absolute;left:236px;width:729px;display:flex}
  .spread--outside{top:38px;height:520px}
  .spread--inside{top:620px;height:516px}
  .panel{position:relative;width:243px;height:100%;overflow:hidden}
  .panel--light{background:var(--paper)}
  .photo{position:absolute;border-radius:7px}
  .photo--dance{background:linear-gradient(160deg,#1d1950 0%,#6a5fb8 45%,#2a244f 100%)}
  .photo--couple{background:linear-gradient(170deg,#2a2b44 0%,#a08d86 50%,#3b2f36 100%)}
  .photo--black{background:#050505}
  .photo--blue{background:linear-gradient(160deg,#2b1f6a,#6c3fa5)}
  .equalizer{position:absolute;left:0;right:0;bottom:0;height:110px;
    background:linear-gradient(to top,rgba(208,26,31,.55),rgba(208,26,31,.15) 60%,rgba(208,26,31,0))}
  /* outside middle */
  .panel--contact{background:linear-gradient(to bottom,#0d0b1e 0%,#0f0c1f 55%,#2a0b10 85%,#0a0608 100%);color:var(--white);text-align:center}
  .burst{position:absolute;left:17px;top:50px;width:210px;height:210px;border-radius:50%;
    background:radial-gradient(circle,rgba(214,40,140,.9) 25%,rgba(120,50,200,.55) 45%,rgba(40,40,160,0) 70%)}
  .badge{position:absolute;left:82px;top:115px;width:80px;height:80px;border-radius:50%;background:var(--white);
    display:flex;align-items:center;justify-content:center;font-weight:700;font-size:14px;color:var(--night)}
  .contact-title{position:absolute;left:70px;top:302px;width:103px;height:23px;border:1px solid #cfcfcf;
    font-size:11px;letter-spacing:1px;line-height:23px}
  .contact-line{position:absolute;left:0;width:100%;font-size:10px;letter-spacing:.5px}
  .contact-phone{font-size:18px;letter-spacing:1px}
  .contact-icon{position:absolute;left:113px;width:16px;height:16px}
  /* cover */
  .panel--cover{background:linear-gradient(to bottom,#0a0a1a 0%,#14123a 35%,#2b2560 55%,#4a1424 78%,#9b1519 92%,#3b0708 100%);color:var(--white)}
  .cover-brand{position:absolute;left:71px;top:52px;width:100px;height:80px;display:flex;flex-direction:column;align-items:center;justify-content:center;gap:6px}
  .cover-brand .dot{width:34px;height:34px;border-radius:50%;background:#1b1b1b;border:1px solid #555}
  .cover-brand .name{font-weight:700;font-size:14px;letter-spacing:1px}
  .script{font-family:"Great Vibes",cursive;font-weight:400}
  .cover-tagline{position:absolute;left:27px;top:272px;font-size:29px;line-height:25px}
  .cover-first{position:absolute;left:27px;top:330px;font-family:"Anton",sans-serif;font-size:76px;line-height:76px;letter-spacing:1px}
  .cover-responders{position:absolute;left:27px;top:408px;font-family:"Anton",sans-serif;font-size:37px;line-height:40px;letter-spacing:.5px}
  .url{position:absolute;left:0;width:100%;text-align:center;font-size:10px;letter-spacing:.6px;color:var(--white)}
  /* inside left */
  .panel--family{background:linear-gradient(to bottom,#0c0c1c 0%,#170d1c 50%,#5a0c12 82%,#b0121a 100%);color:var(--white);text-align:center}
  .family-text{position:absolute;left:0;width:100%}
  .family-script{font-size:21px}
  .family-name{font-weight:700;font-size:15px;letter-spacing:1px}
  .family-plain{font-size:14px;letter-spacing:1.2px}
  /* features */
  .feature-ring{position:absolute}
  .feature-label{position:absolute;font-size:9.5px;line-height:12px;letter-spacing:.3px;color:var(--ink)}
  .feature-label--right{text-align:right}
</style>
</head>
<body>
<svg width="0" height="0" style="position:absolute">
  <defs>
    <filter id="soft" x="-30%" y="-30%" width="160%" height="160%">
      <feDropShadow dx="2" dy="3" stdDeviation="3" flood-color="#000" flood-opacity=".22"/>
    </filter>
    <symbol id="ring" viewBox="-60 -60 120 120">
      <circle r="54" fill="none" stroke="#d01a1f" stroke-width="1.8" stroke-dasharray="95 20 80 144"/>
      <circle r="54" fill="none" stroke="#d01a1f" stroke-width="1.4" stroke-dasharray="1.5 3" transform="rotate(-40)" pathLength="339" style="stroke-dashoffset:0"/>
      <circle cx="-45" cy="-30" r="3" fill="#fff" stroke="#d01a1f" stroke-width="1.3"/>
      <circle cx="42" cy="-34" r="3" fill="#fff" stroke="#d01a1f" stroke-width="1.3"/>
      <circle cx="-46" cy="28" r="3" fill="#fff" stroke="#d01a1f" stroke-width="1.3"/>
      <circle cx="43" cy="33" r="3" fill="#fff" stroke="#d01a1f" stroke-width="1.3"/>
      <circle r="40" fill="#f1f1f1" filter="url(#soft)"/>
      <circle r="31" fill="#fafafa" filter="url(#soft)"/>
    </symbol>
  </defs>
</svg>

<!-- Outside spread -->
<section class="spread spread--outside">
  <div class="panel panel--light">
    <div class="photo photo--dance" style="left:22px;top:15px;width:99px;height:315px" role="img" aria-label="Photo of a groom dancing under blue party lights"></div>
    <div class="photo photo--blue" style="left:129px;top:56px;width:65px;height:58px" role="img" aria-label="Photo of stage lights"></div>
    <div class="photo photo--dance" style="left:129px;top:122px;width:99px;height:315px" role="img" aria-label="Photo of a bride dancing at her reception"></div>
    <div class="photo photo--black" style="left:55px;top:338px;width:65px;height:58px"></div>
    <div class="equalizer" role="img" aria-label="Red dotted equalizer bars"></div>
  </div>

  <div class="panel panel--contact">
    <div class="burst" role="img" aria-label="Pink and blue sound wave burst"></div>
    <div class="badge">Harbor 9</div>
    <div class="contact-title">CONTACT US</div>
    <svg class="contact-icon" style="top:345px" viewBox="0 0 16 16"><rect x="2" y="4" width="12" height="8" fill="#fff"/><path d="M2 4l6 5 6-5" fill="none" stroke="#0d0b1e" stroke-width="1.2"/></svg>
    <p class="contact-line" style="top:363px">Lou@harbor9dj.net</p>
    <svg class="contact-icon" style="top:383px" viewBox="0 0 16 16"><path d="M4 2l3 3-1.5 2a8 8 0 0 0 3.5 3.5L11 9l3 3-2 2C7 14 2 9 2 4z" fill="#fff"/></svg>
    <p class="contact-line contact-phone" style="top:403px">(507) 318-2674</p>
    <svg class="contact-icon" style="top:432px" viewBox="0 0 16 16" fill="none" stroke="#fff" stroke-width="1"><circle cx="8" cy="8" r="6"/><ellipse cx="8" cy="8" rx="2.5" ry="6"/><path d="M2 8h12"/></svg>
    <p class="contact-line" style="top:452px">www.harbor9dj.net</p>
  </div>

  <div class="panel panel--cover" role="img" aria-label="Dance floor with beams of light and red glow">
    <div class="cover-brand"><span class="dot"></span><span class="name">Harbor 9</span></div>
    <p class="cover-tagline script">Owned<br>and operated by</p>
    <p class="cover-first">FIRST</p>
    <p class="cover-responders">RESPONDERS</p>
    <p class="url" style="top:477px">www.harbor9dj.net</p>
  </div>
</section>

<!-- Inside spread -->
<section class="spread spread--inside">
  <div class="panel panel--family">
    <div class="photo photo--couple" style="left:15px;top:58px;width:63px;height:215px" role="img" aria-label="Photo of a laughing groom under confetti"></div>
    <div class="photo photo--couple" style="left:85px;top:98px;width:63px;height:215px" role="img" aria-label="Photo of the couple holding hands"></div>
    <div class="photo photo--couple" style="left:155px;top:58px;width:63px;height:215px" role="img" aria-label="Photo of a laughing bride in lace"></div>
    <p class="family-text family-script script" style="top:345px">When you choose</p>
    <p class="family-text family-name" style="top:372px">HARBOR 9</p>
    <p class="family-text family-script script" style="top:397px">You become part of</p>
    <p class="family-text family-plain" style="top:426px">the first responder family.</p>
    <p class="url" style="top:472px">www.harbor9dj.net</p>
  </div>

  <div class="panel panel--light">
    <svg class="feature-ring" style="left:25px;top:15px;width:130px;height:130px" viewBox="-60 -60 120 120">
      <use href="#ring" x="-60" y="-60" width="120" height="120"/>
      <g fill="none" stroke="#111" stroke-width="1.6"><path d="M0-20v8"/><circle cy="-3" r="8"/><path d="M-4 5h8M-12 12l-4 4M12 12l4 4M0 12v6M-6 14l-2 5M6 14l2 5"/></g>
    </svg>
    <p class="feature-label" style="left:163px;top:64px">LED<br>up lighting.</p>

    <svg class="feature-ring" style="left:122px;top:135px;width:88px;height:88px" viewBox="-60 -60 120 120">
      <use href="#ring" x="-60" y="-60" width="120" height="120"/>
      <circle cy="-10" r="5" fill="#111"/><path d="M0-4v18M-8-16L0-4l8-12M0 14l-4 8" stroke="#111" stroke-width="3" fill="none"/>
    </svg>
    <p class="feature-label feature-label--right" style="right:139px;top:168px">Dancing<br>in the clouds</p>

    <svg class="feature-ring" style="left:22px;top:204px;width:104px;height:104px" viewBox="-60 -60 120 120">
      <use href="#ring" x="-60" y="-60" width="120" height="120"/>
      <g fill="#111"><circle cx="-15" cy="-6" r="3"/><circle cx="-5" cy="-8" r="3"/><circle cx="5" cy="-6" r="3"/><circle cx="15" cy="-8" r="3"/></g>
      <g stroke="#111" stroke-width="3"><path d="M-15-2v12M-5-4v12M5-2v12M15-4v12"/></g>
    </svg>
    <p class="feature-label" style="left:142px;top:247px">Fun, crowd<br>interactive DJ's</p>

    <svg class="feature-ring" style="left:115px;top:304px;width:104px;height:104px" viewBox="-60 -60 120 120">
      <use href="#ring" x="-60" y="-60" width="120" height="120"/>
      <path d="M-5-18h10l-2 5 5 22-8 8-8-8 5-22z" fill="none" stroke="#111" stroke-width="1.5"/>
    </svg>
    <p class="feature-label feature-label--right" style="right:139px;top:346px">Professional<br>reception planning.</p>
    <div class="equalizer" role="img" aria-label="Red dotted equalizer bars"></div>
  </div>

  <div class="panel panel--light">
    <svg class="feature-ring" style="left:22px;top:22px;width:100px;height:100px" viewBox="-60 -60 120 120">
      <use href="#ring" x="-60" y="-60" width="120" height="120"/>
      <g fill="none" stroke="#111" stroke-width="1.8"><rect x="-16" y="-8" width="32" height="16" rx="2"/><circle cx="6" cy="0" r="5"/><path d="M-11-3v6M-7-3v6"/></g>
    </svg>
    <p class="feature-label" style="left:134px;top:60px">Video<br>projection</p>

    <svg class="feature-ring" style="left:88px;top:119px;width:132px;height:132px" viewBox="-60 -60 120 120">
      <use href="#ring" x="-60" y="-60" width="120" height="120"/>
      <g fill="none" stroke="#111" stroke-width="1.6"><path d="M0-20l3 7 7 1-5 5 1 7-6-3-6 3 1-7-5-5 7-1z"/><rect x="-12" y="4" width="24" height="11"/></g>
    </svg>
    <p class="feature-label feature-label--right" style="right:165px;top:164px">Top rated<br>and<br>experienced<br>DJ's</p>

    <svg class="feature-ring" style="left:25px;top:266px;width:144px;height:144px" viewBox="-60 -60 120 120">
      <use href="#ring" x="-60" y="-60" width="120" height="120"/>
      <g stroke="#111" stroke-width="2.4" fill="none"><path d="M-14-10h14M-14-5h12M-14 0h8"/><path d="M6 12v-22c4 0 8 2 8 6"/></g>
      <circle cx="2" cy="12" r="4.5" fill="#111"/>
    </svg>
    <p class="feature-label" style="left:178px;top:314px">Text<br>song<br>request<br>line.</p>
    <div class="equalizer" role="img" aria-label="Red dotted equalizer bars"></div>
  </div>
</section>
</body>
</html>
```